Restaurant Email Club Sign Up Poster

Looking for a creative design that will catch people's eye and prompt them to sign up for our email club for our Restaurant that we run in Omaha, Nebraska. Open to any creative ways to most effectively grab peoples attention quickly without being too confusing. Want it to be simple but actionable.

Have attached some documents for your assistance - in addition to some marketing materials we have put out in the past.

Would like to put design on posters to hang up throughout the restaurant and likely will make stickers to put on check presenters as well.

Catchy stock photo or use of the cheese curd photo probably good idea - callout things mentioned in the "must haves" section below. Looking for most creative and catchy, yet simple design.

Target Market(s)

30-50 year olds males and females.

Industry/Entity Type

Restaurant

Requirements
Must have
• Must include callouts for -
• Sign up for E-Club for access to future offers and events (or something along these lines)
• Free Appetizer for Signing Up
• Free Birthday Meal
Should not have
• Please do not make this poster like the postcard that I attached to the project - this is not a poster to call out that we are a new burger and beer spot, that we have 40 rotating taps, or that we have 15 specialty burgers, etc. This is simply a poster to grab someones attention and get them to sign up for our email club. Should maybe have a catchy question, something like, "Want a Free Appetizer?" or something catchy and similar, and then below say "And access to future deals and event happenings?"

```html
<!DOCTYPE html>
<html lang="en">
<head>
<meta charset="utf-8">
<title>E-Club Sign Up Poster</title>
<link rel="stylesheet" href="https://fonts.googleapis.com/css2?family=Changa+One:ital@1&family=Oswald:wght@600&display=swap">
<style>
  :root {
    --sky: #cdeaf2;
    --paper: #ffffff;
    --gingham: #fde39a;
    --fried-light: #e0a35a;
    --fried-dark: #a8561c;
    --cheese: #f2b33a;
    --red: #c10f1c;
    --ink: #000000;
  }
  html, body {
    margin: 0;
    padding: 0;
    overflow: hidden;
    background: var(--paper);
  }
  .poster {
    display: block;
    width: 849px;
    height: 1200px;
  }
  .sky-band { fill: var(--sky); }
  .paper-band { fill: var(--paper); }
  .gingham-field { fill: var(--gingham); }
  .direction-arrow { fill: var(--ink); }
  .headline {
    font-family: "Changa One", "Arial Black", sans-serif;
    font-style: italic;
    font-size: 92px;
    fill: var(--red);
    letter-spacing: 4px;
  }
  .perk {
    font-family: "Oswald", "Arial Narrow", sans-serif;
    font-weight: 600;
    font-size: 40px;
    fill: var(--red);
  }
</style>
</head>
<body>
<svg class="poster" viewBox="0 0 849 1200" xmlns="http://www.w3.org/2000/svg">
  <defs>
    <linearGradient id="friedGlow" x1="0" y1="0" x2="1" y2="1">
      <stop offset="0" stop-color="var(--cheese)"/>
      <stop offset="0.45" stop-color="var(--fried-light)"/>
      <stop offset="1" stop-color="var(--fried-dark)"/>
    </linearGradient>
  </defs>

  <rect class="paper-band" x="0" y="0" width="849" height="1200"/>
  <polygon class="sky-band" points="0,0 849,0 849,242 0,356"/>

  <polygon class="appetizer-photo" fill="url(#friedGlow)" role="img"
           aria-label="Photo of golden fried cheese curds, one broken open with melted cheese"
           points="0,580 420,440 849,430 849,660 0,770"/>

  <polygon class="gingham-field" role="img" aria-label="Yellow gingham tablecloth pattern"
           points="0,760 849,648 849,1200 0,1200"/>

  <polygon class="direction-arrow" points="271,0 570,0 570,64 613,64 423,232 235,64 271,64"/>
  <polygon class="direction-arrow" points="423,998 613,1140 570,1140 570,1200 271,1200 271,1140 235,1140"/>

  <g class="headline-group" transform="rotate(-8 424 320)">
    <text class="headline" x="410" y="330" text-anchor="middle" textLength="640" lengthAdjust="spacingAndGlyphs">WANT A FREE</text>
    <text class="headline" x="450" y="430" text-anchor="middle" textLength="570" lengthAdjust="spacingAndGlyphs">APPETIZER?</text>
  </g>

  <g class="perks" transform="rotate(-6 424 850)">
    <text class="perk" x="445" y="775" text-anchor="middle" textLength="670" lengthAdjust="spacingAndGlyphs">SIGN UP FOR E-CLUB FOR ACCESS</text>
    <text class="perk" x="445" y="826" text-anchor="middle" textLength="625" lengthAdjust="spacingAndGlyphs">TO FUTURE OFFERS AND EVENTS</text>
    <text class="perk" x="460" y="915" text-anchor="middle" textLength="670" lengthAdjust="spacingAndGlyphs">FREE APPETIZER FOR SIGNING UP</text>
    <text class="perk" x="450" y="1000" text-anchor="middle" textLength="425" lengthAdjust="spacingAndGlyphs">FREE BIRTHDAY MEAL</text>
  </g>
</svg>
</body>
</html>
```